Boom Way Hoist Service Business Cards

I need a business card for "Boom Way Hoist and Haulage"

Boomway2023@hoistmail.net

Hoist Works LLC, Boom Way Hoist and Haulage LLC

555.014.7260 | www.BOOMWAYHOISTS.example

Central Indiana & Northeast Ohio

(IN) 14820 Maple Lane Noblesville, IN 46000

(OH) 2450 Pell Street Akron, Ohio 44300

Colors
0094D4
00A9DD
6FCCEA
C7EBF8
E9F6FB
59FF00
82FF00
B8FF75
E3FFCB
F4FFEA
EE7325
F08F49
F5BC92
FAE3D3
FDF4ED
EB3D1F
EC4F4E
F09395
F8D3D4
FCEDEE
E54698
E96AAD
F1A4CE
F9D9EA
FCEFF6
A7469A
B969AE
D3A5CF
EDDBEB
F8F0F9

```html
<!DOCTYPE html>
<html lang="en">
<head>
<meta charset="utf-8">
<title>Boom Way Hoist and Haulage – Business Card</title>
<link rel="stylesheet" href="https://fonts.googleapis.com/css2?family=Inter:wght@400;700;800&display=swap">
<style>
  :root {
    --page-bg: #e6e6e6;
    --card-white: #ffffff;
    --navy: #1b1f4d;
    --brand-red: #b23a48;
    --ink: #222222;
    --sky-top: #8fb6df;
    --sky-bottom: #d5e4f2;
    --crane-orange: #ee7325;
    --crane-green: #3fae3a;
  }
  * { box-sizing: border-box; margin: 0; padding: 0; }
  html, body { width: 1200px; height: 1200px; overflow: hidden; }
  body {
    background: var(--page-bg);
    font-family: "Inter", Arial, sans-serif;
    display: flex;
    flex-direction: column;
    align-items: center;
    justify-content: center;
    gap: 56px;
  }
  .card {
    position: relative;
    width: 900px;
    height: 518px;
    background: var(--card-white);
    overflow: hidden;
    box-shadow: 0 2px 10px rgba(0,0,0,0.12);
  }

  /* Front */
  .front-photo {
    position: absolute;
    inset: 0 0 34px 0;
    background: linear-gradient(170deg, var(--sky-top) 0%, var(--sky-bottom) 70%, #eef4fa 100%);
  }
  .front-band {
    position: absolute;
    left: 0; right: 0; bottom: 0;
    height: 34px;
    background: var(--navy);
  }
  .front-brand {
    position: absolute;
    left: 520px;
    top: 190px;
    width: 300px;
    display: flex;
    align-items: center;
    gap: 14px;
  }
  .brand-mark {
    width: 26px; height: 26px;
    background: var(--crane-orange);
    flex: none;
  }
  .brand-name {
    font-weight: 800;
    font-size: 40px;
    line-height: 1.05;
    color: var(--navy);
    letter-spacing: 0.5px;
  }

  /* Back */
  .back-brand {
    position: absolute;
    left: 60px;
    top: 190px;
    width: 220px;
    display: flex;
    align-items: center;
    gap: 12px;
  }
  .back-brand .brand-name { font-size: 34px; }
  .divider {
    position: absolute;
    left: 300px;
    top: 140px;
    width: 2px;
    height: 222px;
    background: var(--brand-red);
  }
  .contact {
    position: absolute;
    left: 352px;
    top: 156px;
    list-style: none;
    font-size: 23px;
    color: var(--ink);
    line-height: 1;
  }
  .contact li {
    display: flex;
    align-items: center;
    height: 35px;
  }
  .contact .icon {
    width: 20px; height: 20px;
    margin-right: 10px;
    flex: none;
  }
  .contact .address { margin-top: 12px; height: 37px; }
  .back-bands {
    position: absolute;
    left: 0; bottom: 0;
    width: 900px;
    height: 44px;
  }
</style>
</head>
<body>

  <section class="card card-front" aria-label="Card front">
    <div class="front-photo" role="img" aria-label="Photograph of a blue crane boom lifting an orange personnel basket against a cloudy blue sky"></div>
    <div class="front-brand">
      <span class="brand-mark"></span>
      <span class="brand-name">Boom Way</span>
    </div>
    <div class="front-band"></div>
  </section>

  <section class="card card-back" aria-label="Card back">
    <div class="back-brand">
      <span class="brand-mark"></span>
      <span class="brand-name">Boom Way</span>
    </div>
    <div class="divider"></div>
    <ul class="contact">
      <li>
        <svg class="icon" viewBox="0 0 24 24" aria-hidden="true"><path fill="#1b1f4d" d="M6.6 10.8a15.1 15.1 0 0 0 6.6 6.6l2.2-2.2a1 1 0 0 1 1-.25 11.4 11.4 0 0 0 3.6.57 1 1 0 0 1 1 1V20a1 1 0 0 1-1 1A17 17 0 0 1 3 4a1 1 0 0 1 1-1h3.5a1 1 0 0 1 1 1c0 1.25.2 2.45.57 3.57a1 1 0 0 1-.25 1z"/></svg>
        555.014.7260
      </li>
      <li>
        <svg class="icon" viewBox="0 0 24 24" aria-hidden="true"><rect x="2" y="5" width="20" height="14" rx="1.5" fill="#1b1f4d"/><path d="M3 6.5l9 6 9-6" fill="none" stroke="#fff" stroke-width="1.6"/></svg>
        Boomway2023@hoistmail.net
      </li>
      <li>
        <svg class="icon" viewBox="0 0 24 24" aria-hidden="true"><circle cx="12" cy="12" r="10" fill="#1b1f4d"/><g fill="none" stroke="#fff" stroke-width="1.3"><ellipse cx="12" cy="12" rx="4.2" ry="9.5"/><path d="M2.5 12h19M4 7h16M4 17h16"/></g></svg>
        www.BOOMWAYHOISTS.example
      </li>
      <li class="address">(IN) 14820 Maple Lane Noblesville, IN 46000</li>
      <li>(OH) 2450 Pell Street Akron, Ohio 44300</li>
    </ul>
    <svg class="back-bands" viewBox="0 0 900 44" aria-hidden="true">
      <polygon points="0,0 500,0 540,44 0,44" fill="#1b1f4d"/>
      <polygon points="512,10 900,10 900,44 546,44" fill="#b23a48"/>
    </svg>
  </section>

</body>
</html>
```